Anzeigengestaltung für Vermittlung von 24h-Pflegekräften
Zielgruppe
Wir vermitteln 24h Pflegekräfte
Zielgruppe sind zu Betreuende und deren Angehörige
Aufgabenstellung
Ich benötige eine Anzeige einer 1/4 A4 Seite.
übersichtlich und schön gestaltet, geradlinig und professionell
Das bild von Gerda Lenzmayr und Stefan Lenzmayr soll untergebracht werden + ÜWS31 Logo + BetreuHaus Logo
Wenn möglich auch das Bild mit der helfenden Hand auch (wenn es sich vom Platz her ausgeht)

```html
<!DOCTYPE html>
<html lang="de">
<head>
<meta charset="utf-8">
<title>BetreuHaus – Anzeige 24h Betreuung</title>
<link href="https://fonts.googleapis.com/css2?family=Montserrat:wght@400;500;600;700;800&display=swap" rel="stylesheet">
<style>
  :root {
    --navy: #0f4a80;
    --navy-deep: #0b3f73;
    --text-blue: #1d4f86;
    --orange: #e8701a;
    --white: #ffffff;
    --canvas: #ececec;
  }
  * { margin: 0; padding: 0; box-sizing: border-box; }
  html, body { width: 1200px; height: 2286px; overflow: hidden; }
  body { background: var(--canvas); font-family: "Montserrat", sans-serif; position: relative; }

  .ad {
    position: absolute; left: 60px; top: 380px;
    width: 777px; height: 1098px;
    transform: scale(1.39); transform-origin: top left;
    background: var(--white); overflow: hidden;
    box-shadow: 0 10px 30px rgba(0,0,0,.12);
  }
  .abs { position: absolute; }

  .brand { left: 55px; top: 92px; display: flex; align-items: center; gap: 10px; }
  .brand-dot { width: 18px; height: 18px; border-radius: 50%; background: var(--orange); }
  .brand-name { font-size: 26px; font-weight: 600; color: var(--navy); }

  .company { right: 50px; top: 40px; text-align: right; }
  .company-name { font-size: 23px; font-weight: 700; color: var(--orange); line-height: 30px; }
  .company-line { font-size: 17px; font-weight: 500; color: var(--navy); line-height: 28px; }
  .company-dots { margin-top: 6px; display: flex; justify-content: flex-end; gap: 8px; }
  .company-dots span { width: 5px; height: 5px; background: var(--navy); }

  .photo-care { left: 53px; top: 186px; width: 210px; height: 143px; border-radius: 14px;
    background: linear-gradient(135deg, #dcdedb 0%, #d6b9a3 55%, #b8704f 100%); }
  .photo-hands { left: 53px; top: 345px; width: 210px; height: 142px; border-radius: 14px;
    background: linear-gradient(135deg, #d3e2e4 0%, #e3c9b6 55%, #c9dadd 100%); }
  .photo-team { left: 345px; top: 208px; width: 385px; height: 295px; border-radius: 10px;
    background: linear-gradient(180deg, #eef1f6 0%, #d5dceb 45%, #3f4f86 75%, #2d3b63 100%); }

  .web-pill { left: 32px; top: 538px; width: 248px; height: 29px; border-radius: 15px;
    background: var(--orange); color: var(--white); font-size: 17px; font-weight: 700;
    display: flex; align-items: center; justify-content: center; }

  .badge-24h { left: 79px; top: 624px; width: 162px; height: 162px; border-radius: 50%;
    background: radial-gradient(circle at 35% 25%, #3a86c4, var(--navy-deep) 75%);
    color: var(--white); display: flex; flex-direction: column; align-items: center; justify-content: center; }
  .badge-24h .big { font-size: 56px; font-weight: 600; line-height: 56px; }
  .badge-24h .small { font-size: 14px; font-weight: 800; letter-spacing: .3px; margin-top: 2px; }

  .features { left: 313px; top: 519px; list-style: none; width: 430px; }
  .features li { position: relative; padding-left: 30px; font-size: 17px; font-weight: 500;
    color: var(--text-blue); line-height: 34px; }
  .features li::before { content: ""; position: absolute; left: 0; top: 13px;
    width: 9px; height: 9px; border-radius: 50%; background: var(--navy); }

  .wave { left: 0; top: 850px; width: 777px; height: 248px; }

  .photo-duo { left: 20px; top: 808px; width: 310px; height: 290px; border-radius: 60px 60px 0 0;
    background: linear-gradient(180deg, #c9a595 0%, #3f51a3 55%, #2b3458 100%); }

  .seal { left: 650px; top: 845px; width: 114px; height: 114px; border-radius: 50%;
    background: var(--white); border: 4px solid var(--navy); box-shadow: inset 0 0 0 12px #2d5fa8; }

  .owners { left: 342px; top: 918px; color: var(--white); }
  .owners-name { font-size: 22px; font-weight: 700; line-height: 31px; }
  .owners-text { margin-top: 14px; font-size: 18px; font-weight: 500; line-height: 25px; width: 410px; }
  .owners-text strong { font-weight: 800; }
</style>
</head>
<body>
  <article class="ad">
    <div class="abs brand">
      <span class="brand-dot"></span>
      <span class="brand-name">BetreuHaus</span>
    </div>

    <div class="abs company">
      <div class="company-name">BetreuHaus GmbH</div>
      <div class="company-line">7132 Frauenkirchen Lindengasse 14</div>
      <div class="company-line">0664 / 517 328 40 – 02175 / 38219</div>
      <div class="company-dots"><span></span><span></span><span></span><span></span><span></span><span></span><span></span></div>
    </div>

    <div class="abs photo-care" role="img" aria-label="Foto: Pflegerin mit älterer Dame"></div>
    <div class="abs photo-hands" role="img" aria-label="Foto: helfende Hand hält die Hand einer älteren Person"></div>
    <div class="abs photo-team" role="img" aria-label="Foto: Gruppenbild des Betreuungsteams"></div>

    <div class="abs web-pill">www.betreuhaus.at</div>

    <div class="abs badge-24h">
      <span class="big">24h</span>
      <span class="small">BETREUUNG</span>
    </div>

    <ul class="abs features">
      <li>Laufende Qualitätskontrolle einer<br>diplomierten Krankenschwester (DGKP)</li>
      <li>ÜWS-31 zertifiziert gemäß den Richtlinien<br>des Sozialministeriums</li>
      <li>Vermittlung von qualifiziertem Personal<br>im Burgenland, Niederösterreich &amp; Wien</li>
      <li>Übernahme sämtlicher Behördenwege &amp;<br>Bürokratie</li>
      <li>Laufende Begleitung und Beratung</li>
      <li>Erfahrung seit 2010</li>
    </ul>

    <svg class="abs wave" viewBox="0 0 777 248" preserveAspectRatio="none" aria-hidden="true">
      <path d="M0 38 C 120 85, 230 75, 330 40 C 450 12, 600 30, 777 22 L777 248 L0 248 Z" fill="var(--orange)"/>
      <path d="M0 57 C 120 100, 230 92, 330 58 C 450 30, 600 48, 777 42 L777 248 L0 248 Z" fill="var(--navy)"/>
    </svg>

    <div class="abs photo-duo" role="img" aria-label="Foto: Gerda Lenzmayr und Stefan Lenzmayr"></div>

    <div class="abs seal" role="img" aria-label="Gütesiegel ÜWS31"></div>

    <div class="abs owners">
      <div class="owners-name">DGKS Gerda Lenzmayr</div>
      <div class="owners-name">Stefan Lenzmayr</div>
      <p class="owners-text">sind gemeinsam mit ihrem Team seit über <strong>10 Jahren</strong> im Burgenland, NÖ und Wien in der 24h Betreuung tätig!</p>
    </div>
  </article>
</body>
</html>
```